business card with logo Velmora Nails & Spa 2816 SW Quillan Ave Portland OR 97384

Would like to have a business card with our logo.
like bottle of polish with our logo or letter V on it
want something that first glance would let you know that it is a nail salon.
like the hands with polish bottle dripping.
like black or White back ground

Velmora Nails & Spa
(The Velvet Retreat)
2816 SW Quillan Ave
Portland, OR 97384
Call or Text: 1-503-555-0148
www.VelmoraNailsnSpa.example
Open 7 days a week.
After 7:00 PM is by appointment only.
Closed only on Thanksgiving & Christmas.

Target Market(s)

20%Man and 80%Woman 13-70

Industry/Entity Type

Business

Contact Information for Business Card

Elegant with Logo-Business name- address-phone-open days. closed day.

Font styles to use
Decorative
Script

Colors
000000

Requirements
Must have
• Logo and place for Technician Name
• Velmora Nails & Spa
• (The Velvet Retreat)
• 2816 SW Quillan Ave
• Portland, OR 97384
• Call or Text: 1-503-555-0148
• Open 7 days a week
• Closed only on Thanksgiving & Christmas.
• We accepted all major credit cards but prefer cash. Thank you
Nice to have
• Nail polish bottle with our Logo or letter V
Should not have
• too colorful

```html
<!DOCTYPE html>
<html lang="en">
<head>
<meta charset="utf-8">
<title>Velmora Nails &amp; Spa – Business Card</title>
<link rel="stylesheet" href="https://fonts.googleapis.com/css2?family=Gelasio:wght@400&display=swap">
<style>
  :root {
    --stage: #2f2a27;
    --card: #1f2022;
    --card-edge: #2a2b2e;
    --pink: #ef5f93;
    --pink-soft: #b8577c;
    --silver: #d9d9d9;
    --grey: #b5b5b5;
    --paper: #ffffff;
    --chip: #c9c9c9;
    --ink: #1f2022;
  }
  * { box-sizing: border-box; margin: 0; padding: 0; }
  html, body {
    width: 1200px; height: 780px; overflow: hidden;
    background: var(--stage);
    font-family: "Gelasio", Georgia, serif;
  }
  .canvas { position: relative; width: 1200px; height: 780px; }

  .card {
    position: absolute;
    width: 540px; height: 309px;
    background: var(--card);
    border: 1px solid var(--card-edge);
    border-radius: 3px;
    box-shadow: 0 12px 30px rgba(0,0,0,.45);
  }
  .card--front { left: 70px; top: 80px; }
  .card--back  { left: 590px; top: 390px; }

  /* Hands and polish bottle artwork area */
  .artwork {
    display: block;
    border-radius: 6px;
    background: linear-gradient(135deg, rgba(217,217,217,.35) 0%, rgba(239,95,147,.55) 100%);
  }
  .brand__name { color: var(--silver); line-height: 1.1; white-space: nowrap; }

  /* Front */
  .card--front .artwork { position: absolute; left: 115px; top: 78px; width: 90px; height: 80px; }
  .card--front .brand__name { position: absolute; left: 215px; top: 128px; font-size: 28px; }
  .site { color: var(--grey); font-size: 15px; }
  .site__name { color: var(--pink); }
  .card--front .site { position: absolute; left: 0; right: 0; top: 212px; text-align: center; }

  /* Back */
  .tech { position: absolute; left: 30px; top: 28px; }
  .tech__name { color: var(--pink); font-size: 18px; letter-spacing: .5px; }
  .tech__role { color: var(--grey); font-size: 13px; margin-top: 2px; }

  .info { position: absolute; left: 30px; top: 102px; color: var(--grey); font-size: 13.5px; line-height: 1.4; }
  .info__address { font-style: normal; margin-bottom: 14px; }
  .info__hours { list-style: none; }
  .info .site { font-size: 13.5px; margin-top: 4px; }

  .card--back .brand {
    position: absolute; right: 26px; top: 84px;
    display: flex; flex-direction: column; align-items: flex-end;
  }
  .card--back .artwork { width: 76px; height: 64px; margin-right: 110px; }
  .card--back .brand__name { font-size: 20px; margin-top: 8px; }
  .brand__tagline { color: var(--grey); font-size: 12px; margin-top: 3px; }

  .payments {
    position: absolute; right: 22px; bottom: 18px;
    width: 196px; background: var(--paper); padding: 6px 8px 8px;
  }
  .payments__note { color: var(--ink); font-size: 9px; line-height: 1.25; margin-bottom: 5px; }
  .payments__cards { display: flex; gap: 6px; }
  .payments__card { width: 40px; height: 22px; background: var(--chip); border-radius: 3px; }
</style>
</head>
<body>
<main class="canvas">
  <section class="card card--front" aria-label="Card front">
    <span class="artwork" role="img" aria-label="Illustration of two hands with a dripping nail polish bottle"></span>
    <span class="brand__name">Velmora Nails &amp; Spa</span>
    <p class="site">www.<span class="site__name">VelmoraNailsnSpa</span>.example</p>
  </section>

  <section class="card card--back" aria-label="Card back">
    <div class="tech">
      <p class="tech__name">TECHNICIAN NAME</p>
      <p class="tech__role">Nail Technician</p>
    </div>
    <div class="info">
      <address class="info__address">2816 SW Quillan Ave<br>Portland, OR 97384</address>
      <ul class="info__hours">
        <li>- Call or Text: 1-503-555-0148</li>
        <li>- Open 7 days a week</li>
        <li>- Closed only on Thanksgiving &amp; Christmas.</li>
      </ul>
      <p class="site">www.<span class="site__name">VelmoraNailsnSpa</span>.example</p>
    </div>
    <div class="brand">
      <span class="artwork" role="img" aria-label="Illustration of two hands with a dripping nail polish bottle"></span>
      <span class="brand__name">Velmora Nails &amp; Spa</span>
      <span class="brand__tagline">(The Velvet Retreat)</span>
    </div>
    <div class="payments">
      <p class="payments__note">We accept all major credit cards but prefer cash. Thank you</p>
      <div class="payments__cards">
        <span class="payments__card"></span>
        <span class="payments__card"></span>
        <span class="payments__card"></span>
        <span class="payments__card"></span>
      </div>
    </div>
  </section>
</main>
</body>
</html>
```